Reaching the Root: Reasoning in Clinical Choice-Making

I'd like a cover that looks like it would fit on the shelf next to "The Symptom Mirage" by Harold Vintner, "The Fall of Forgetting" by Carl Mortenson, "Meal Mend" by Neil Forsby, "The Energy Renewal Plan" by Owen Prichardson or "The Gland Renewal Plan" by the same or "The Cortex Renewal Plan" by the same ... either text only (with some interesting fonts that make the title stand out, and the subtitle smaller) or a relevant image, though I'm not entirely sure what that would be since this is a book about big-picture medical decision making.
Author name is Dr Miriam Oakhurst, NMD
I'll eventually request an e-book, paperback, and audio cover from the winner...

Target Market(s)

practicing physicians

Industry/Entity Type

medicine

Requirements
Must have
• look similar to other books in the genre

```html
<!DOCTYPE html>
<html lang="en">
<head>
<meta charset="utf-8">
<title>Reaching the Root — Book Cover</title>
<link rel="stylesheet" href="https://fonts.googleapis.com/css2?family=Ubuntu:wght@500&family=Arimo:wght@400;700&display=swap">
<style>
  :root {
    --page-bg: #ffffff;
    --cover-bg: #fbf6f7;
    --ink: #231f20;
    --accent-red: #e52b1a;
    --panel-light: #f1eeee;
    --panel-red: #c8281b;
  }
  html, body {
    margin: 0;
    padding: 0;
    width: 1200px;
    height: 1200px;
    overflow: hidden;
    background: var(--page-bg);
  }
  .canvas {
    position: relative;
    width: 1200px;
    height: 1200px;
  }
  .book-cover {
    position: absolute;
    left: 230px;
    top: 44px;
    width: 740px;
    height: 1112px;
    background: var(--cover-bg);
  }
  .book-cover svg {
    display: block;
    width: 740px;
    height: 1112px;
  }
  .title-top {
    font-family: "Ubuntu", "Trebuchet MS", sans-serif;
    font-weight: 500;
    fill: var(--ink);
  }
  .title-main {
    font-family: "Ubuntu", "Trebuchet MS", sans-serif;
    font-weight: 500;
    fill: var(--accent-red);
  }
  .subtitle {
    font-family: "Arimo", Arial, sans-serif;
    font-weight: 400;
    fill: var(--ink);
  }
  .subtitle .highlight {
    font-weight: 700;
    fill: var(--accent-red);
  }
  .author {
    font-family: "Arimo", Arial, sans-serif;
    font-weight: 400;
    fill: var(--ink);
  }
</style>
</head>
<body>
<main class="canvas">
  <section class="book-cover">
    <svg viewBox="0 0 740 1112" xmlns="http://www.w3.org/2000/svg">
      <defs>
        <radialGradient id="feature-fill" cx="50%" cy="50%" r="50%">
          <stop offset="0%" stop-color="var(--panel-red)"/>
          <stop offset="55%" stop-color="var(--panel-red)"/>
          <stop offset="75%" stop-color="#e9dcdb"/>
          <stop offset="100%" stop-color="var(--panel-light)"/>
        </radialGradient>
      </defs>

      <text class="title-top" x="68" y="174" font-size="100"
            textLength="594" lengthAdjust="spacingAndGlyphs">REACHING THE</text>
      <text class="title-main" x="68" y="406" font-size="270"
            textLength="590" lengthAdjust="spacingAndGlyphs">ROOT</text>

      <text class="subtitle" x="82" y="480" font-size="30"
            textLength="590" lengthAdjust="spacingAndGlyphs">REASONING IN <tspan class="highlight">CLINICAL</tspan> CHOICE-MAKING</text>

      <rect class="feature-image" x="120" y="534" width="495" height="404"
            fill="url(#feature-fill)" role="img"
            aria-label="Torn white paper revealing a red surface with a white question mark"/>

      <text class="author" x="82" y="1042" font-size="42"
            textLength="580" lengthAdjust="spacingAndGlyphs">DR MIRIAM OAKHURST, NMD</text>
    </svg>
  </section>
</main>
</body>
</html>
```